'Cradle Ahead' promotional brochure

We have designed a 6 week program to educate impending first-time parents about the things they need to know to survive the first 6 months. Sessions delivered by general practitioner/family doctor, dietician, physiotherapist, speech pathologist and psychologist. Our promotional blurb is: 'A comprehensive education program for first-time parents-to-be, delivered over 6 weeks by health professionals in your community, about everything you need to know to look after your baby (and yourself!) in the first 6 months'. I now want to put together a promotional brochure to be distributed to those couples who express an interest which will provide further details of what will be delivered in the course.
Updates
In terms of layout, I envisaged a double sided A4 size, foldable into 3 sections, but very happy to be guided on this.
Target Market(s)
To appeal to a young, well educated demographic. First time parents couples.
Industry/Entity Type
Medical
Font styles to use
Other font styles liked:
- Playfair Display
Requirements
Must have
- Playfair display font to be consistent with our logo (attached). Logo also included please. Some consistency with colours of logo please.
Nice to have
- I am a doctor, and have no creative genes! But prefer a clean and professional appearance overall. Not too cluttered in overall appearance.
Should not have
- No cheesy pictures of babies.

```html
<!DOCTYPE html>
<html lang="en">
<head>
<meta charset="utf-8">
<title>Cradle Ahead – Brochure</title>
<link rel="stylesheet" href="https://fonts.googleapis.com/css2?family=Playfair+Display:wght@400;700&family=Roboto+Slab:wght@300;400&family=Roboto:wght@400;500&display=swap">
<style>
:root{
  --green:#8dc63f;
  --green-light:#c9e39b;
  --ink:#3d3d3d;
  --body:#8a8a8a;
  --rule:#9a9a9a;
  --paper:#ffffff;
  --paper-soft:#f6f6f6;
  --backdrop:#2c2c2c;
  --stripe:#ececec;
}
*{margin:0;padding:0;box-sizing:border-box}
html,body{width:720px;height:1200px;overflow:hidden;background:var(--backdrop)}
.canvas{position:relative;width:720px;height:1200px}
.sheet{position:absolute;left:38px;width:644px;height:456px;display:flex;box-shadow:0 4px 14px rgba(0,0,0,.45)}
.sheet--outer{top:112px}
.sheet--inner{top:668px}
.panel{position:relative;height:100%;overflow:hidden;font-family:"Roboto Slab",serif;font-weight:300;color:var(--body);font-size:7.2px;line-height:1.5}
.panel--w1{width:213px}.panel--w2{width:218px}.panel--w3{width:213px}
.panel--white{background:var(--paper)}
.panel--soft{background:linear-gradient(90deg,#f1f1f1,#fff 12%,#fff 88%,#f3f3f3)}
.panel--green{background:var(--green);color:#fff}
.stripes{position:absolute;pointer-events:none}
.week{position:absolute;display:inline-block;background:var(--green);color:#fff;font-family:"Playfair Display",serif;font-weight:700;font-size:11.5px;line-height:17px;height:17px;padding:0 13px;border-radius:9px}
.week--white{background:#fff;color:var(--green)}
.block{position:absolute;left:18px;right:16px;text-align:justify}
.session{font-weight:400;color:var(--ink);margin-bottom:5px}
.u{border-bottom:.7px solid var(--rule)}
.topics{list-style:none;margin-top:12px}
.topics li{position:relative;padding-left:14px;letter-spacing:.3px}
.topics li::before{content:"";position:absolute;left:1px;top:4px;width:4px;height:4px;border-radius:50%;background:#9a9a9a}
.panel--green .topics li::before{background:#fff}
.brand{position:absolute;display:flex;align-items:center;gap:6px;font-family:"Roboto Slab",serif;font-weight:400;color:var(--green);letter-spacing:.6px;text-transform:uppercase}
.brand__dot{width:20px;height:20px;background:var(--green)}
.contact{position:absolute;left:0;right:0;text-align:center}
.contact__label{top:384px;font-weight:400;font-size:8.2px;color:var(--ink)}
.contact__phone{top:404px;font-family:"Roboto",sans-serif;font-weight:500;font-size:22px;color:var(--green);letter-spacing:.3px}
.photo{position:absolute}
.photo--hands{left:22px;top:0;right:0;height:264px;border-bottom-left-radius:160px 130px;background:radial-gradient(ellipse at 50% 55%,#e9c8b4,#f1ddd0 45%,#f7efe9 80%)}
.photo--feeding{left:0;top:0;right:0;height:220px;background:linear-gradient(180deg,#e6dcd6 0%,#efe7e2 45%,#f8f5f3 80%,#fff 100%)}
.photo--parents{left:40px;top:292px;right:0;bottom:0;background:linear-gradient(180deg,#fff 0%,#d9d6d4 30%,#bdb8b5 100%)}
.hero-title{position:absolute;left:0;right:0;top:278px;text-align:center;font-family:"Playfair Display",serif;font-size:22px;letter-spacing:3.5px;line-height:25px;color:var(--ink)}
.hero-sub{position:absolute;left:0;right:0;text-align:center;font-family:"Roboto Slab",serif;font-weight:400;color:var(--ink)}
.pill-white{display:inline-block;background:#fff;border-radius:12px;padding:2px 14px}
.intro{position:absolute;left:0;right:0;text-align:center;color:var(--ink);font-family:"Roboto Slab",serif;font-weight:300}
.dash{position:absolute;left:72px;width:74px;top:236px;border-top:1px dashed rgba(255,255,255,.7)}
</style>
</head>
<body>
<div class="canvas">

  <!-- OUTER SIDE -->
  <section class="sheet sheet--outer">
    <div class="panel panel--w1 panel--white">
      <svg class="stripes" style="left:120px;top:0" width="100" height="60" viewBox="0 0 100 60"><g stroke="var(--stripe)" stroke-width="11" stroke-linecap="round"><line x1="20" y1="-5" x2="50" y2="45"/><line x1="48" y1="-5" x2="78" y2="45"/></g></svg>
      <svg class="stripes" style="left:0;top:380px" width="110" height="80" viewBox="0 0 110 80"><g stroke="var(--stripe)" stroke-width="11" stroke-linecap="round"><line x1="12" y1="20" x2="45" y2="75"/><line x1="45" y1="20" x2="78" y2="75"/></g></svg>
      <span class="week" style="left:18px;top:70px">Week 4</span>
      <div class="block" style="top:93px">
        GP Dr Helen Marsh will share advice about <span class="u">your babies' health in the first 6 months,</span> including:
        <ul class="topics">
          <li>Skin of newborns</li><li>Sleeping</li><li>Crying</li><li>Immunisations</li><li>Fever and infections</li><li>Diarrhoea and constipation</li><li>Teething</li><li>Understanding a baby's signals</li>
        </ul>
      </div>
      <span class="week" style="left:18px;top:278px">Week 5</span>
      <div class="block" style="top:301px">
        <p class="session">Session 1</p>
        <p>Clinical Psychologist Dr Nadia Brooks will share information about <span class="u">bonding &amp; attachment with your baby,</span> how to <span class="u">promote their social &amp;</span> emotional development and how to manage separation anxiety. She will also discuss positive parenting approaches.</p>
      </div>
    </div>

    <div class="panel panel--w2 panel--soft">
      <svg class="stripes" style="left:130px;top:0" width="80" height="90" viewBox="0 0 80 90"><g stroke="var(--stripe)" stroke-width="10" stroke-linecap="round" fill="none"><path d="M20 15 H60 V70"/></g><circle cx="30" cy="52" r="10" fill="var(--stripe)"/></svg>
      <span class="week" style="left:19px;top:70px">Week 6</span>
      <div class="block" style="top:94px;left:19px">
        <p class="session">Session 1</p>
        <p>Secret Men's Business – <span class="u">a men-only session (including beer!)</span> with a new father for frank discussion about the road ahead. Mums will do a shopping excursion with the GP &amp; Dietician to Harvest Market to look at baby products and food – the good and the bad!</p>
        <p class="session" style="margin-top:10px">Session 2</p>
        <p>Program review, reflection and evaluation and <span class="u">future session planning when baby is 6 months of age.</span></p>
      </div>
      <div class="brand" style="left:52px;top:302px;font-size:9.5px;line-height:12px">
        <span class="brand__dot"></span><span style="color:var(--ink)">Wattle Grove<br><span style="color:var(--green)">Health</span></span>
      </div>
      <p class="contact contact__label">Contact Details for Enquries / Bookings</p>
      <p class="contact contact__phone">(02)5550 1234</p>
    </div>

    <div class="panel panel--w3 panel--green">
      <div class="photo photo--hands" role="img" aria-label="Photo of parents' hands cradling a newborn's foot"></div>
      <div class="brand" style="left:128px;top:14px;font-size:7.5px;line-height:10px;gap:4px">
        <span class="brand__dot" style="width:12px;height:12px"></span><span style="color:var(--ink)">Wattle Grove<br>Health</span>
      </div>
      <h1 class="hero-title">CRADLE<br>—AHEAD—</h1>
      <p class="hero-sub" style="top:342px;font-size:8.4px">A comprehensive educational program</p>
      <p class="hero-sub" style="top:357px;font-size:9.6px"><span class="pill-white">For First-Time Parents-To-Be</span></p>
      <p class="hero-sub" style="top:384px;font-size:8px">delivered</p>
      <p class="hero-sub" style="top:397px;font-family:'Playfair Display',serif;font-weight:700;font-size:13px;letter-spacing:.5px">OVER 6 WEEKS</p>
      <p class="hero-sub" style="top:416px;font-size:7.8px">by health professionals in your community</p>
    </div>
  </section>

  <!-- INNER SIDE -->
  <section class="sheet sheet--inner">
    <div class="panel panel--w1 panel--green">
      <svg class="stripes" style="left:120px;top:0" width="100" height="60" viewBox="0 0 100 60"><g stroke="rgba(255,255,255,.28)" stroke-width="11" stroke-linecap="round"><line x1="20" y1="-5" x2="50" y2="45"/><line x1="48" y1="-5" x2="78" y2="45"/></g></svg>
      <p class="intro" style="top:86px;font-size:9.6px;line-height:13px">We provide a complete<br>education about everything<br>you need to know to look after</p>
      <p class="intro" style="top:132px;font-family:'Playfair Display',serif;font-size:21px;letter-spacing:1.5px"><span class="pill-white" style="border-radius:16px;padding:0 14px;line-height:30px">your baby</span></p>
      <p class="intro" style="top:178px;font-size:16px;line-height:24px;font-weight:400">(and yourself!)<br>in the first 6 months</p>
      <div class="dash"></div>
      <span class="week week--white" style="left:18px;top:296px">Week 1</span>
      <div class="block" style="top:318px;color:#fff">
        GP Dr Helen Marsh willshare information for <span class="u" style="border-color:#fff">Mum's own health after delivery.</span> Topics include:
        <ul class="topics" style="margin-top:10px">
          <li>Vaccinations in pregnancy</li><li>Bleeding, bladder and bowel after delivery</li><li>Breastfeeding, engorgement and mastitis</li><li>Bottle feeding</li><li>Post-natal anxiety &amp; depression</li><li>Intimacy and contraception</li>
        </ul>
      </div>
    </div>

    <div class="panel panel--w2 panel--white">
      <div class="photo photo--feeding" role="img" aria-label="Photo of a baby being bottle fed"></div>
      <span class="week" style="left:19px;top:232px">Week 2</span>
      <div class="block" style="top:254px;left:19px">
        <p class="session">Session 1</p>
        <p>Clinical Psychologist Dr Nadia Brooks will discuss <span class="u">changes in relationships as couples becomes parents,</span> gender roles in parenting and post-natal depression.</p>
        <p class="session" style="margin-top:10px">Session 2</p>
        <p>Physiotherapist Laura Pike will present advice for Mums regarding <span class="u">exercise during and after pregnancy, looking after the pelvic floor during and after pregnancy,</span> and abdominal muscle separation management. She will also provide advice for promoting babies' neck strength and minimising the risk of flat spots on the head and encouraging gross motor skills in the first 6 months.</p>
      </div>
    </div>

    <div class="panel panel--w3 panel--white">
      <svg class="stripes" style="left:120px;top:0" width="100" height="60" viewBox="0 0 100 60"><g stroke="var(--green-light)" stroke-width="11" stroke-linecap="round" opacity=".7"><line x1="20" y1="-5" x2="50" y2="45"/><line x1="48" y1="-5" x2="78" y2="45"/></g></svg>
      <span class="week" style="left:18px;top:61px">Week 3</span>
      <div class="block" style="top:83px">
        <p class="session">Session 1</p>
        <p>Dietician Clare Whitby provides advice for Mums regarding <span class="u">healthy eating during pregnancy and lactation, normal weight gain during pregnancy</span> and realistic weight loss after. She will also discuss the evidence regarding breastfeeding VS bottle-feeding, normal infant weight gain and introducing solids (including those with potential for allergy).</p>
        <p class="session" style="margin-top:10px">Session 2</p>
        <p>Paediatric Speech Pathologist Ruth Calder will share information about <span class="u">latching and breast-feeding troubles &amp; tongue tie,</span> advice about dummies and finger-sucking, introducing solids &amp; feeding (including 'pouch' food), encouraging language development and current evidence about electronic devices impacting language development.</p>
      </div>
      <div class="photo photo--parents" role="img" aria-label="Soft photo of two parents leaning over a newborn"></div>
    </div>
  </section>

</div>
</body>
</html>
```